Every Drawer Neatly Sorted or EDN Organized needs a business card design. EDN Organized is a professi

We need a business card design that is clean, sharp and conveys a sense of organization. I already have a logo.

Target Market(s)

Families (specifically mothers), small business owners, parents, seniors

Industry/Entity Type

Business

Contact Information for Business Card

My website is www.ednorganized-example.com and my Facebook page is http://www.socialpage-example.com/everydrawerneatlysorted. The phone number is 555-418-2706 and I want to be listed as Miriel O. Dunsford, Owner

Requirements
Must have
• My logo.

```html
<!DOCTYPE html>
<html lang="en">
<head>
<meta charset="utf-8">
<title>Every Drawer Neatly Sorted – Business Card</title>
<link rel="stylesheet" href="https://fonts.googleapis.com/css2?family=Arimo:wght@400;700&display=swap">
<style>
  :root {
    --brand-blue: #0b7fe0;
    --ink: #2a2f36;
    --paper: #ffffff;
    --paper-shade: #eef0f3;
    --backdrop: #e6e8ec;
  }
  * { box-sizing: border-box; margin: 0; padding: 0; }
  html, body { width: 1200px; height: 891px; overflow: hidden; }
  body {
    background: var(--backdrop);
    font-family: "Arimo", Arial, sans-serif;
    position: relative;
  }
  .card {
    position: absolute;
    left: 340px;
    width: 520px;
    height: 297px;
    box-shadow: 0 6px 18px rgba(0,0,0,.18);
    overflow: hidden;
  }
  /* Front side */
  .card-front {
    top: 116px;
    background: radial-gradient(ellipse at 55% 45%, var(--paper) 35%, var(--paper-shade) 100%);
  }
  .brand {
    position: absolute;
    top: 64px;
    right: 40px;
    display: flex;
    align-items: center;
    gap: 10px;
  }
  .brand-mark {
    width: 12px; height: 12px;
    background: var(--ink);
  }
  .brand-name {
    font-size: 18px;
    font-weight: 400;
    color: var(--ink);
    white-space: nowrap;
  }
  .rule {
    position: absolute; left: 0; right: 0;
    height: 2px; background: var(--brand-blue);
  }
  .rule-top { top: 146px; }
  .rule-bottom { top: 234px; }
  .band {
    position: absolute; left: 0; right: 0;
    top: 152px; height: 76px;
    background: var(--brand-blue);
    color: var(--paper);
    display: flex;
    align-items: center;
    justify-content: space-between;
    padding: 0 18px 0 22px;
  }
  .person { white-space: nowrap; }
  .person-name { font-size: 21px; font-weight: 700; line-height: 1.1; }
  .person-role { font-size: 15px; font-weight: 400; text-align: right; padding-right: 6px; }
  .contact-list { list-style: none; font-size: 9.5px; line-height: 1.6; white-space: nowrap; }
  .contact-list li { display: flex; align-items: center; gap: 6px; }
  .contact-icon {
    width: 10px; height: 10px;
    background: var(--paper);
    display: inline-flex; align-items: center; justify-content: center;
    flex: none;
  }
  .contact-icon svg { width: 8px; height: 8px; }
  /* Back side */
  .card-back {
    top: 478px;
    background: var(--brand-blue);
    color: var(--paper);
    display: flex; flex-direction: column;
    align-items: center; justify-content: center;
  }
  .back-name { font-size: 23px; font-weight: 700; letter-spacing: .5px; }
  .back-role { font-size: 16px; font-weight: 400; letter-spacing: 1px; margin-top: 2px; }
</style>
</head>
<body>
  <section class="card card-front">
    <div class="brand">
      <span class="brand-mark"></span>
      <span class="brand-name">Every Drawer Neatly Sorted</span>
    </div>
    <div class="rule rule-top"></div>
    <div class="band">
      <div class="person">
        <div class="person-name">Miriel O. Dunsford</div>
        <div class="person-role">Owner</div>
      </div>
      <ul class="contact-list">
        <li>
          <span class="contact-icon">
            <svg viewBox="0 0 10 10"><path d="M2 1 L4 1 L4.6 3.2 L3.5 4 Q4.5 6 6 6.5 L6.8 5.4 L9 6 L9 8 Q8.5 9 7.5 9 Q1 8 1 2.5 Q1 1 2 1Z" fill="#0b7fe0"/></svg>
          </span>555 - 418 - 2706
        </li>
        <li>
          <span class="contact-icon">
            <svg viewBox="0 0 10 10"><circle cx="5" cy="5" r="3.8" fill="none" stroke="#0b7fe0" stroke-width="1"/><path d="M1.2 5 H8.8 M5 1.2 Q2.5 5 5 8.8 M5 1.2 Q7.5 5 5 8.8" fill="none" stroke="#0b7fe0" stroke-width=".8"/></svg>
          </span>www.ednorganized-example.com
        </li>
        <li>
          <span class="contact-icon"></span>www.socialpage-example.com/everydrawerneatlysorted
        </li>
      </ul>
    </div>
    <div class="rule rule-bottom"></div>
  </section>

  <section class="card card-back">
    <div class="back-name">Miriel O. Dunsford</div>
    <div class="back-role">Owner</div>
  </section>
</body>
</html>
```